Modern/Bold/Unique Prenatal Vitamin label redesign

We are in need of a design update for our Prenatal Vitamin label. We want to modernize our label and give it a fresh feel.
It should bring a feeling of fun, joy, and sophistication, but also be bold/edgy/unique and portray Trust and Authority. Our buyers are mainly mothers in the age range of 25-34 who are pregnant or breastfeeding.
I will attach our current label design, as well as some inspiration to go off of.
We like the idea of having a clean, easy to read label label with bold/vibrant colors and fonts. We like the idea of having some retro vibes in it as well
Please see the attached artwork for design inspiration (New Design Idea). We like the idea of having a pregnant mother image like the attachment on the label, with the rest of the label being white. Please come up with a unique drawing/image for the design. We cannot use a copied image or stock image.
We look forward to working with you!

```html
<!DOCTYPE html>
<html lang="en">
<head>
<meta charset="utf-8">
<title>Bloomi Nest – Prenatal Bloom Label</title>
<link rel="stylesheet" href="https://fonts.googleapis.com/css2?family=Figtree:wght@400;600;700;800&display=swap">
<style>
  :root {
    --brand-pink: #e61e78;
    --ink: #333333;
    --paper: #ffffff;
    --ring: #b5b5b5;
    --art-violet: #6d5bb8;
    --art-rose: #e64a86;
    --art-blue: #3d56a6;
  }
  * { margin: 0; padding: 0; box-sizing: border-box; }
  html, body { width: 998px; height: 1200px; overflow: hidden; background: var(--paper); }
  body { font-family: "Figtree", sans-serif; color: var(--ink); }
  .label { position: relative; width: 998px; height: 1200px; background: var(--paper); overflow: hidden; }

  .brand-name {
    position: absolute; left: 82px; top: 96px;
    font-family: "Figtree", sans-serif; font-weight: 800;
    font-size: 92px; line-height: 1; letter-spacing: -1px;
    color: var(--brand-pink);
  }

  .mother-art {
    position: absolute; left: 660px; top: 67px; width: 322px; height: 835px;
  }

  .product-name {
    position: absolute; left: 78px; top: 420px;
    font-weight: 700; font-size: 78px; line-height: 1; letter-spacing: -0.5px;
    color: var(--ink);
  }
  .product-tagline {
    position: absolute; left: 79px; top: 506px;
    font-weight: 400; font-size: 40px; line-height: 53px;
    color: var(--ink);
  }

  .footer-band { position: absolute; left: 0; top: 0; width: 998px; height: 1200px; }

  .count {
    position: absolute; left: 373px; top: 807px; width: 248px; height: 248px;
    display: flex; align-items: center; justify-content: center;
    font-weight: 800; font-size: 118px; letter-spacing: -3px; color: var(--ink);
  }

  .supplement-type {
    position: absolute; left: 82px; top: 1012px;
    font-weight: 600; font-size: 45px; line-height: 54px; color: var(--paper);
  }
  .capsule-type {
    position: absolute; left: 583px; top: 1062px;
    font-weight: 600; font-size: 45px; line-height: 54px; color: var(--paper);
  }
</style>
</head>
<body>
<main class="label">
  <div class="brand-name">Bloomi Nest</div>

  <svg class="mother-art" viewBox="0 0 322 835" role="img" aria-label="Colourful speckled silhouette illustration of a pregnant mother in profile">
    <defs>
      <linearGradient id="artTone" x1="0" y1="0" x2="0.4" y2="1">
        <stop offset="0" stop-color="var(--art-violet)"/>
        <stop offset="0.5" stop-color="var(--art-rose)"/>
        <stop offset="1" stop-color="var(--art-blue)"/>
      </linearGradient>
    </defs>
    <rect x="0" y="0" width="322" height="835" rx="40" fill="url(#artTone)"/>
  </svg>

  <h1 class="product-name">Prenatal Bloom</h1>
  <p class="product-tagline">Once Daily Premium<br>Multivitamin for<br>Mama &amp; Baby</p>

  <svg class="footer-band" viewBox="0 0 998 1200" aria-hidden="true">
    <path d="M0,900 C150,892 290,898 380,940 L616,940 C700,902 850,898 998,900 L998,1200 L0,1200 Z" fill="var(--brand-pink)"/>
    <circle cx="497" cy="931" r="124" fill="var(--paper)" stroke="var(--ring)" stroke-width="2"/>
  </svg>

  <div class="count">90</div>

  <p class="supplement-type">Dietary<br>Supplement</p>
  <p class="capsule-type">Veggie Capsules</p>
</main>
</body>
</html>
```